Simple templates for management consulting firm

Vireo Advisors is a management consulting firm based in the DC area. We have all the basic templates but would like to tweak them so they look consistent.

Check us out at www.vireoadvisors-example.com

For this project we would like to get
a tweaked powerpoint template (header should be up)
a letter template for letters
a fax template

Current templates and our logo are attached.
Updates

We just increased the budget of this project.

We got questions about the project. Here are our thoughts on this one:

Please include the logo into the fax template. If you find improvements in the layout then feel free to make those. Let's not overthink this too much. Keep it simple :)

We like The powerpoint concept as is. The slide titles are for some reasons on the bottom. It seems to irritate some folks. If you can switch the slide titles to the top, keep the look and feel of the slides and work in the logo then that would be fantastic.

The letter head should include the following

Vireo Advisors, LLC Box 5817, Pine Hollow, VA 20499 Phone 555 814-2906, Fax 555 276 9143, www.vireoadvisors-example.com and the logo.

Again, let's keep it simple.

Thank you for considering this project.

We just realize that we are not necessarily inisting to use the red in the slides.
Any approach that would work with the logo will be considered.

Thanks for your creativity.

Target Market(s)

tech companies, Meridian 400, venture capitalists

Industry/Entity Type

Management Consulting

Requirements
Must have
• Keep it simple please

```html
<!DOCTYPE html>
<html lang="en">
<head>
<meta charset="utf-8">
<title>Vireo Advisors Letterhead</title>
<link href="https://fonts.googleapis.com/css2?family=PT+Sans&family=Cinzel:wght@400&display=swap" rel="stylesheet">
<style>
  :root {
    --page: #fefefe;
    --header-band: #e1e1e1;
    --footer-rule: #c6c6c6;
    --brand-ink: #6f6f6f;
    --mark-fill: #8a8a8a;
    --footer-ink: #2a2a2a;
  }
  html, body {
    margin: 0;
    padding: 0;
    overflow: hidden;
  }
  body {
    width: 928px;
    height: 1200px;
    background: var(--page);
    position: relative;
  }
  .letterhead-band {
    position: absolute;
    left: 54px;
    top: 54px;
    width: 826px;
    height: 112px;
    background: var(--header-band);
    display: flex;
    align-items: center;
  }
  .brand {
    display: flex;
    align-items: center;
    gap: 16px;
    margin-left: 12px;
  }
  .brand-mark {
    width: 84px;
    height: 84px;
    border-radius: 50%;
    background: var(--mark-fill);
  }
  .brand-name {
    font-family: "Cinzel", serif;
    font-size: 38px;
    font-weight: 400;
    color: var(--brand-ink);
    letter-spacing: 1px;
  }
  .footer-rule {
    position: absolute;
    left: 47px;
    top: 1095px;
    width: 841px;
    height: 10px;
    background: var(--footer-rule);
  }
  .footer-contact {
    position: absolute;
    left: 0;
    top: 1110px;
    width: 928px;
    text-align: center;
    font-family: "PT Sans", sans-serif;
    font-size: 13px;
    line-height: 16px;
    color: var(--footer-ink);
    margin: 0;
  }
</style>
</head>
<body>
  <header class="letterhead-band">
    <div class="brand">
      <span class="brand-mark"></span>
      <span class="brand-name">Vireo Advisors</span>
    </div>
  </header>

  <div class="footer-rule"></div>
  <p class="footer-contact">
    Vireo Advisors, LLC Box 5817 Pine Hollow, VA 20499 &bull; Phone 555 814-2906 Fax 555 276 9143<br>
    www.vireoadvisors-example.com
  </p>
</body>
</html>
```